Educational Brochure or Pamphlet Series

We are a nonprofit organization looking at revamping our template designs for our educational pamphlet series, as we edit and republish our content library for 2014. Most of the current content spans over 3 to 4 panel double-sided folded brochures, although we are not limited to that format moving forward. We would be looking for a design that is inviting prompting interest at initial pick up, while also being laid out in a manner where complex tips and advice is able to be digested by readers. We do not have a consistent brand currently among our materials so we are able to branch to a new more modern and professional look/theme, but at the same time i wouldn't want to to go so far away from our look that we clash with our colors/logo/identity.

I almost chose magazine as project type, because ideally i would prefer a design that has the ability to grow beyond a 3 panel foldable brochure, into a small multipage booklet or magazine bound style.

We are a nonprofit in the health advocacy realm that helps patients understand the insurance and medical industry so they can get and afford the care they need while battling a major illness. We have not updated our publication design in over 10 years and need a professional refresh. More about us can be found at www.carewaybridge.org
Updates

Thanks to everyone that has already contributed designs or those who have accepted the project invite and are still working on submission.    I appreciate your willingness to assist our organization and participate in the process.   I look forward to reviewing the designs soon.

I am excited to participate in my first project on Pixel Harbor, and look forward to working again on future projects within this platform.

If you have any questions or could benefit from additional explanation on aspects of the project, please feel free to reach out to me and I'd be happy to share any insight I have.

Marna

Target Market(s)

Our pamphlets and brochures are geared towards patients who have been diagnosed with serious illness (ex. cancer, ALS, MS) and who are navigating the healthcare system to get the care and medications they need. Patients or caregivers would pick up these brochures in cancer facilities, doctors office or through online research.

Included in uploaded files are a few of these current pamphlets, some of our more recently designed ads or promo pieces to see what we have been doing lately. If needed and requested, i'd be happy to provide links of some of the brochures of our favorite partners who have done a nice job with presenting similar information.

Industry/Entity Type

Insurance

Font styles to use
Sans Serif

Colors

Designer to choose colors to be used in the design.

Requirements
Must have
• -Information easy to read and digest
-professional and educational in focus
-a design that can be reasonably customized or modified to include a number of corollary topics in a similar structure to complete a full library.
-colorful (can be 2 color or 4 color print)
-enough white space to be pleasing to the eye and not overwhelming with text
Nice to have
• could work on a lighthouse or beacon of light theme. (possible, ok if not)
Should not have
• ideally no extreme die cuts or printing specs that would be exceptionally expensive to produce, given nonprofit budget

```html
<!DOCTYPE html>
<html lang="en">
<head>
<meta charset="utf-8">
<title>A Greater Understanding – Careway Bridge Foundation brochure</title>
<link href="https://fonts.googleapis.com/css2?family=Open+Sans:wght@400;600;700&family=Roboto+Condensed:wght@400;700&display=swap" rel="stylesheet">
<style>
:root{
  --navy:#1d3a8a;
  --blue:#1b6fb8;
  --sky:#dbeaf6;
  --sky-edge:#b9d5ec;
  --gold:#f6b21d;
  --orange:#f08a1c;
  --ink:#3a3a3a;
  --dark:#1c1f35;
  --paper:#ffffff;
  --stage:#3b3430;
}
*{box-sizing:border-box;margin:0;padding:0}
html,body{width:865px;height:1200px;overflow:hidden}
body{background:var(--stage);font-family:"Open Sans",Arial,sans-serif;color:var(--ink);position:relative}
.page{position:absolute;width:367px;height:516px;background:var(--paper);overflow:hidden;box-shadow:0 3px 10px rgba(0,0,0,.45)}
.p1{left:48px;top:68px}
.p2{left:436px;top:68px}
.p3{left:48px;top:610px}
.p4{left:436px;top:610px}
p{font-size:6.6px;line-height:1.42;text-align:justify;margin-bottom:5px}
h2{font-family:"Roboto Condensed",Arial,sans-serif;color:var(--navy);font-weight:700;font-size:14px;line-height:1.1;margin-bottom:6px}
.brand{display:flex;align-items:center;gap:5px;font-family:"Open Sans",Arial,sans-serif;font-weight:700;line-height:1}
.brand-mark{width:14px;height:14px;background:var(--gold)}
.brand-sub{font-size:3.4px;color:#555;margin-top:2px}

/* page 1 */
.masthead{position:absolute;left:0;top:0;width:100%;height:68px;background:var(--dark);display:flex;align-items:center;padding-left:108px}
.masthead .brand{color:#fff;font-size:11px}
.address-bar{position:absolute;left:0;top:68px;width:100%;height:13px;background:var(--navy);color:#fff;font-size:6px;text-align:right;padding:2px 12px 0 0}
.title{position:absolute;left:0;top:95px;width:100%;text-align:center;font-family:"Roboto Condensed",Arial,sans-serif;font-weight:700;color:var(--blue);font-size:30px;letter-spacing:-.3px}
.promo{position:absolute;left:28px;top:138px;width:310px;height:52px;border:2px solid var(--orange);border-radius:8px;background:var(--sky);display:flex;overflow:hidden}
.promo .photo{width:84px;height:100%;background:linear-gradient(135deg,#cfe3f1,#e9dccb 60%,#b9d2e6)}
.promo-text{flex:1;text-align:center;font-family:"Roboto Condensed",Arial,sans-serif;color:var(--navy);font-size:12.5px;line-height:1.15;padding-top:9px}
.facts-head{position:absolute;left:12px;top:200px;font-family:"Roboto Condensed",Arial,sans-serif;font-weight:700;color:var(--navy);font-size:12px}
.facts{position:absolute;left:12px;top:218px;width:343px;column-count:2;column-gap:12px;height:110px}
.facts p{margin-bottom:3px}
.facts strong{color:#222}
.family{position:absolute;left:12px;top:332px;width:165px;height:105px;background:linear-gradient(160deg,#eef2f5,#d9c3ad 55%,#f4efe9)}
.young{position:absolute;left:188px;top:328px;width:167px;text-align:center}
.young h3{font-family:"Roboto Condensed",Arial,sans-serif;font-weight:400;color:var(--blue);font-size:13px;line-height:1.1}
.young em{display:block;font-size:9px;color:#333;margin:3px 0 8px;line-height:1.25}
.young .org{font-weight:700;color:var(--navy);font-size:8px;margin-bottom:3px}
.young .addr{font-size:5.8px;line-height:1.45;color:#444}
.footer-band{position:absolute;left:0;bottom:0;width:100%;height:80px}
.footer-band svg{position:absolute;inset:0}
.footer-band .slogan{position:absolute;left:12px;top:30px;font-family:"Roboto Condensed",Arial,sans-serif;font-weight:700;color:var(--navy);font-size:12px;line-height:1.2}

/* inner pages */
.top-wave{position:absolute;left:0;top:0;width:100%;height:34px}
.url{position:absolute;right:14px;top:9px;font-size:7.5px;font-weight:700;color:#222}
.bottom-wave{position:absolute;left:0;bottom:0;width:100%;height:22px}
.col-left{position:absolute;left:14px;top:40px;width:166px}
.panel{position:absolute;left:190px;top:44px;width:163px;background:var(--sky);border-radius:6px;padding:6px 8px}
.panel-title{background:#fff;text-align:center;font-family:"Roboto Condensed",Arial,sans-serif;font-weight:700;color:var(--blue);font-size:14px;padding:4px 0;margin:-2px -2px 7px;border-radius:3px}
.ph{width:100%;margin-bottom:7px;border-radius:2px}
.doctor{height:64px;background:linear-gradient(120deg,#c9d7e4,#e8ecef 50%,#a8b8c8)}
.nurse{height:58px;background:linear-gradient(120deg,#e8eef3,#9fc3de 55%,#f1f4f6)}
.exam{height:48px;background:linear-gradient(150deg,#8fb8d8,#e6eef4 60%,#bcd3e4)}
.foot-brand{position:absolute;left:14px;bottom:22px}
.foot-brand .brand{color:var(--gold);font-size:10px}
.call{font-family:"Roboto Condensed",Arial,sans-serif;font-weight:700;color:var(--blue);font-size:15px;line-height:1.2;margin-top:8px}
.tower{position:absolute;left:188px;top:48px;width:166px;height:455px;background:linear-gradient(180deg,#5a87c4 0%,#9dbde0 55%,#7c9a5a 88%,#4d6b35 100%)}
</style>
</head>
<body>

<!-- Front cover -->
<section class="page p1">
  <header class="masthead">
    <div class="brand"><span class="brand-mark"></span><div>Careway Bridge<br>Foundation</div></div>
  </header>
  <div class="address-bar">118 Linden Mill Road, Harbor City, VA 23600</div>
  <h1 class="title">A Greater Understanding</h1>
  <div class="promo">
    <div class="photo" role="img" aria-label="Photo of a smiling older couple"></div>
    <div class="promo-text">Promoting A Healthier<br>Africal American Community</div>
  </div>
  <div class="facts-head">Facts and Circumstances Relating to the Individual</div>
  <div class="facts">
    <p><strong>The purpose of this brochure is to address questions surrounding Second Opinions:</strong></p>
    <p>Knowing Your Rights and Options. Making decisions about healthcare is one of the most important in a person's life. Many people are told that they have cancer or another life threatening illness and feel that they must make a decision and begin treatment as soon as possible. While this may be true in some instances, taking the time to learn about your disease, getting a second opinion or perhaps even a third opinion and weighing your options is a very reasonable approach. Proactive decision making will give you a greater degree of control over your treatment. Decisions regarding your health should be made after you have been thoroughly informed about your diagnosis, prognosis and available treatment options.</p>
  </div>
  <div class="family" role="img" aria-label="Photo of a smiling family of four"></div>
  <div class="young">
    <h3>Health Insurance for<br>Young Adults:</h3>
    <em>Why you need it &amp;<br>How to Keep it</em>
    <div class="org">Careway Bridge Foundation</div>
    <div class="addr">540 Quarry Point Blvd, Suite 300<br>Bayport, VA 23610<br>Phone: 1-800-555-0142, Fax: 757-555-0187<br>Email: help@carewaybridge.org</div>
  </div>
  <div class="footer-band">
    <svg viewBox="0 0 367 80" preserveAspectRatio="none" aria-hidden="true">
      <path d="M0 22 Q180 4 367 16 L367 80 L0 80Z" fill="var(--gold)"/>
      <path d="M0 18 Q180 0 367 12" fill="none" stroke="var(--blue)" stroke-width="2"/>
      <path d="M0 68 Q200 58 367 62 L367 80 L0 80Z" fill="var(--orange)"/>
    </svg>
    <div class="slogan">Solving Insurance and<br>Healthcare Access Problem Since 1996</div>
  </div>
</section>

<!-- Page 2 -->
<section class="page p2">
  <svg class="top-wave" viewBox="0 0 367 34" preserveAspectRatio="none" aria-hidden="true">
    <path d="M0 4 L367 4 L367 20 Q180 30 0 22Z" fill="var(--gold)"/>
    <path d="M0 26 Q180 34 367 22" fill="none" stroke="var(--blue)" stroke-width="1.5"/>
  </svg>
  <div class="url">www.carewaybridge.org</div>
  <div class="col-left">
    <h2>Will my Doctor be upset if I get a second opinion?</h2>
    <p>Most doctors will welcome another physician's input. Your doctor may be able to recommend a specialist. A good doctor understands your right to be well informed and should support a second opinion. You will want to obtain a copy of your medical records and test results, to share with the new doctor.</p>
    <h2>Doctor's opinions may differ</h2>
    <p>A different doctor may come up with a different diagnosis, or at least offer a different opinion as to treatment choices. Not every doctor will have the same opinion with regard to diseases and possible treatments. Factors which may have an effect on a doctor's opinion are technology available to that doctor, school of thought, where they were trained, individual methods of treatment and experience in dealing with that particular diagnosis.</p>
    <h2>Treatment methods may differ</h2>
    <p>Some doctors prefer to monitor the situation and use less aggressive procedures before moving to surgical intervention. Some doctors like to use more aggressive treatment methods from the beginning. By getting a second opinion, you can expand your options about different treatment methods which may be most suitable for you and your situation. Being informed is always your best option!</p>
  </div>
  <aside class="panel">
    <div class="panel-title">Choosing a Physician</div>
    <div class="ph doctor" role="img" aria-label="Photo of a doctor in a white coat"></div>
    <p>There are many professional doctors in practice today. Family physicians provide comprehensive medical care with an emphasis on caring for all members of the family. A general surgeon is able to perform all types of surgical procedures aimed at treating a range of diseases and conditions, including cancer. Medical oncologists are specialists that use various medications to treat and manage patients with cancer. This may include the use of chemotherapy to kill cancer cells, painkillers to manage cancer pain, and drugs that will eliminate or reduce the side effects of cancer treatment.</p>
    <p>Radiation oncologists use therapeutic applications of radiation to manage cancer and other diseases. They determine the type of radiation that will be used, as well as the amount or dose, and the number and length of treatments. You may have a need for all four of these types of physicians at one time. It is beneficial to you to keep files or a journal with names and dates and copies of your medical records and procedures as your journey to wellness can be confusing and the doctors will need to know exactly what care you have previously received.</p>
  </aside>
  <svg class="bottom-wave" viewBox="0 0 367 22" preserveAspectRatio="none" aria-hidden="true">
    <path d="M0 8 Q180 20 367 6" fill="none" stroke="var(--blue)" stroke-width="1.5"/>
  </svg>
</section>

<!-- Page 3 -->
<section class="page p3">
  <svg class="top-wave" viewBox="0 0 367 34" preserveAspectRatio="none" aria-hidden="true">
    <path d="M0 4 L367 4 L367 20 Q180 30 0 22Z" fill="var(--gold)"/>
    <path d="M0 26 Q180 34 367 22" fill="none" stroke="var(--blue)" stroke-width="1.5"/>
  </svg>
  <div class="url">www.carewaybridge.org</div>
  <div class="col-left">
    <h2>Second opinions don't hurt and in fact may even help</h2>
    <p>It never hurts to get a second opinion. Keep in mind that doctors are human and they too can make mistakes or be faced with unusual or challenging cases. When the first doctor's opinion is the same or similar to the second doctor's, your confidence will be increased. There is nothing lost by visiting one more doctor just to make sure that the first doctor's opinion is correct. With serious illnesses that may require extended treatment, you should feel confident that you have chosen the most appropriate treatment for your particular situation. A valid opinion and appropriate course of treatment is your best option for return to good health or grasping control of the chronic disease.</p>
    <p>While second opinions may be awkward for doctor and patient at times, studies have shown that 30 percent of patients, who sought second opinions for elective surgery and 18 percent of those who were required to obtain a second opinion by their insurance company, found that the two opinions were not in agreement. These studies are one more reason why you need to make sure you are educated properly to make the best decision for your health.</p>
    <div class="ph nurse" role="img" aria-label="Photo of a nurse caring for a patient"></div>
  </div>
  <aside class="panel">
    <div class="panel-title">Patient Rights</div>
    <div class="ph doctor" role="img" aria-label="Photo of a medical team in discussion"></div>
    <p>Second opinions are a way to learn about your diagnosis and choices for treatment options. Some doctors are more conservative while others tend to be more aggressive. A patient has rights and one of your most important rights is the right to get a second opinion about your diagnosis. Being informed is critical in deciding your choice of treatment.</p>
    <p>Statistics show that over one third of adults in the United States will never seek a second opinion and almost one tenth of newly diagnosed patients rarely, or never understand their diagnosis. A second opinion means you are consulting with another doctor to confirm a diagnosis and/or find possible different treatment choices available to you. It is recommended to get a second opinion immediately to avoid delays in your treatment and recovery. Seven states currently have health laws pertaining to second opinions.</p>
    <div class="ph exam" role="img" aria-label="Photo of a doctor examining a patient"></div>
  </aside>
  <div class="foot-brand"><div class="brand"><span class="brand-mark"></span><div>Careway Bridge<br>Foundation<div class="brand-sub">Solving Insurance and Healthcare Access Problems | Since 1996</div></div></div></div>
</section>

<!-- Page 4 -->
<section class="page p4">
  <svg class="top-wave" viewBox="0 0 367 34" preserveAspectRatio="none" aria-hidden="true">
    <path d="M0 4 L367 4 L367 20 Q180 30 0 22Z" fill="var(--gold)"/>
    <path d="M0 26 Q180 34 367 22" fill="none" stroke="var(--blue)" stroke-width="1.5"/>
  </svg>
  <div class="url">www.carewaybridge.org</div>
  <div class="col-left">
    <h2>What will it cost me?</h2>
    <p>Assuming it is medically necessary, most insurance plans will pay for at least part of the cost while Medi-Plan will pay 80% of the cost. As a matter of fact if the second opinion doesn't agree with the first, Medi-Plan will pay 80% of the cost of a third opinion. Patients that belong to a Health Maintenance Organization (HMO) are entitled to a second opinion, but some plans require a referral from your primary care physician, and like most HMO treatments, you must see an in-network physician. To learn about second opinions call 1-800-MEDIPLAN (1-800-555-0199) or for specific rules by state for a second opinion you can visit www.mediplan-info.gov/coverage/home.asp</p>
    <p>Call your insurance provider before going for any treatment or second opinion to prevent any confusion or denial of the bill. You need to know exactly what will be covered, such as an out of network provider, any lab work or testing that may be required and what your responsibilities are before seeking the second opinion. Diagnostic tests can be very costly and many insurance providers will not pay for them if they were completed for the initial diagnosis. You have the right to have copies of the tests you already had done. Be an informed consumer and arrive for the second opinion with all of your previous medical records, contact information about the first physician, insurance card, list of prescribed medications and allergies, and any diagnostic test results.</p>
    <div class="call">Call 1-800-MEDIPLAN<br>(1-800-555-0199)</div>
  </div>
  <div class="tower" role="img" aria-label="Photo of a black and white spiral striped lighthouse against a blue sky"></div>
  <div class="foot-brand"><div class="brand"><span class="brand-mark"></span><div>Careway Bridge<br>Foundation<div class="brand-sub">Solving Insurance and Healthcare Access Problems | Since 1996</div></div></div></div>
</section>

</body>
</html>
```